Commercial Landscaping Flyer Needed

Looking for a flyer design to showcase what we offer for commercial landscape Installations. We want this to illustrate what sets us apart from our competitors. Include our EMR Safety rating of .72, that our average commercial landscape installation size is $215,000 with our largest completed in 2020 being $1,375,590. We have backgrounds in commercial design and installation and help our customers with Value Engineering Strategies. Since incorporating in 2005, we have an average employment retention length of 8 years. We want this flyer to show our commercial clients that we mean business and are dedicated to making their project happen on time, run efficiently, and we do excellent work.

Need extra days to review

```html
<!DOCTYPE html>
<html lang="en">
<head>
<meta charset="utf-8">
<title>Greenway Grounds – Commercial Landscaping Flyer</title>
<link rel="stylesheet" href="https://fonts.googleapis.com/css2?family=Cabin+Condensed:wght@500;700&family=Montserrat:wght@700&family=Source+Sans+3:wght@300;400&display=swap">
<style>
:root{
  --green:#c2da35;
  --green-pale:#f4f8e7;
  --charcoal:#343434;
  --ink:#1b1b1b;
  --white:#ffffff;
  --backdrop:#e4e4e4;
}
*{margin:0;padding:0;box-sizing:border-box}
html,body{width:1200px;height:686px;overflow:hidden}
body{background:var(--backdrop);position:relative;font-family:"Source Sans 3",sans-serif;color:var(--ink)}
.page{position:absolute;top:37px;width:472px;height:611px;background:var(--white);overflow:hidden;box-shadow:0 2px 8px rgba(0,0,0,.25)}
.page--front{left:102px}
.page--back{left:625px}
.page svg.shapes{position:absolute;left:0;top:0}

/* front */
.brand{position:absolute;left:27px;top:62px;display:flex;align-items:center;gap:8px}
.brand__dot{width:30px;height:30px;border-radius:50%;background:var(--green)}
.brand__name{font-family:"Cabin Condensed",sans-serif;font-weight:700;font-size:24px;color:var(--ink);line-height:1}
.headline{position:absolute;right:28px;top:30px;text-align:right;font-family:"Cabin Condensed",sans-serif;font-weight:700;font-size:27px;line-height:33px;color:var(--white)}
.intro{position:absolute;left:28px;top:122px;width:212px;font-size:9px;line-height:11.1px}
.facts{position:absolute;left:28px;top:523px;width:160px;font-family:"Cabin Condensed",sans-serif;font-weight:700;color:var(--green)}
.facts__since{font-size:11.5px;padding-bottom:7px;border-bottom:1px solid #d8d8d8}
.facts__retention{font-size:11.5px;line-height:14px;margin-top:8px}

/* back */
.stats{position:absolute;left:28px;top:25px;width:118px;font-family:"Cabin Condensed",sans-serif;font-weight:700;font-size:12.4px;line-height:13.2px;color:var(--ink);white-space:nowrap}
.stats__item{padding:0 0 10px}
.stats__item + .stats__item{border-top:1px solid var(--white);padding-top:10px}
.stats__item:first-child{line-height:14.6px;padding-bottom:10px}
.section-title{font-family:"Montserrat",sans-serif;font-weight:700;color:var(--green);font-size:13px;line-height:15.5px}
.services{position:absolute;left:28px;top:262px;width:230px}
.bullets{list-style:none;margin-top:6px}
.bullets li{position:relative;padding-left:15px;font-size:9px;line-height:12.65px;white-space:nowrap}
.bullets li::before{content:"";position:absolute;left:2px;top:4.8px;width:3px;height:3px;border-radius:50%;background:var(--green)}
.services__copy{position:absolute;left:28px;top:424px;width:222px;font-size:8px;line-height:10.2px}
.clients{position:absolute;left:295px;top:293px;width:170px}
.clients .bullets{margin-top:7px}
.contact{position:absolute;left:0;top:520px;width:276px;height:91px;background:var(--charcoal);border-top:4px solid #111;color:var(--white)}
.contact__col{position:absolute;top:12px;font-size:6.8px;line-height:8.4px}
.contact__col--company{left:28px}
.contact__col--offices{left:130px}
.contact__rule{position:absolute;left:108px;top:14px;width:1px;height:32px;background:var(--white)}
.contact__label{color:var(--green);font-weight:400}
.contact__web{position:absolute;left:28px;top:56px;font-weight:300;font-size:15px;letter-spacing:2px;color:var(--green);white-space:nowrap}
</style>
</head>
<body>

<section class="page page--front">
  <svg class="shapes" width="472" height="611" viewBox="0 0 472 611">
    <defs>
      <linearGradient id="cityGrad" x1="0" y1="0" x2="0" y2="1">
        <stop offset="0" stop-color="#9fb6cc"/>
        <stop offset=".45" stop-color="#7a6a5c"/>
        <stop offset="1" stop-color="#6f9a4a"/>
      </linearGradient>
      <linearGradient id="stripGrad" x1="0" y1="0" x2="0" y2="1">
        <stop offset="0" stop-color="#a9c3de"/>
        <stop offset=".45" stop-color="#9a9a92"/>
        <stop offset="1" stop-color="#5f8a3c"/>
      </linearGradient>
    </defs>
    <rect x="0" y="227" width="472" height="384" fill="#111"/>
    <rect x="0" y="508" width="472" height="103" fill="var(--charcoal)"/>
    <rect role="img" aria-label="Photo of a finished roadside lawn and curb planting" x="0" y="232" width="300" height="85" fill="url(#stripGrad)"/>
    <rect role="img" aria-label="Photo of a storefront with new mulched planting beds" x="0" y="325" width="300" height="83" fill="url(#stripGrad)"/>
    <rect role="img" aria-label="Photo of a landscaped highway median with young trees" x="0" y="416" width="300" height="84" fill="url(#stripGrad)"/>
    <circle cx="368" cy="90" r="118" fill="var(--green)"/>
    <rect x="400" y="90" width="72" height="340" fill="var(--green)"/>
    <circle cx="340" cy="424" r="214" fill="var(--green)"/>
    <circle role="img" aria-label="Aerial photo of a downtown apartment courtyard with turf, planters and seating" cx="340" cy="432" r="184" fill="url(#cityGrad)"/>
  </svg>

  <div class="brand">
    <span class="brand__dot"></span>
    <span class="brand__name">greenway grounds</span>
  </div>

  <h1 class="headline">15 Years<br>of Professional<br>Landscaping!</h1>

  <p class="intro">Greenway Grounds specializes in Commercial Projects, offering design build options as well as bidding services in many scopes of work. Let us provide the finishing details to bring the project full circle, including sod, seed, landscaping and irrigation. Greenway Grounds prides itself in getting the job done correctly and ahead of schedule to aid in the overall success of the project.</p>

  <div class="facts">
    <p class="facts__since">Since 2005</p>
    <p class="facts__retention">Average employment<br>retention length of 8 years</p>
  </div>
</section>

<section class="page page--back">
  <svg class="shapes" width="472" height="611" viewBox="0 0 472 611">
    <defs>
      <linearGradient id="gardenGrad" x1="0" y1="0" x2="0" y2="1">
        <stop offset="0" stop-color="#3f6a2c"/>
        <stop offset=".45" stop-color="#8d8a78"/>
        <stop offset=".75" stop-color="#c9a43a"/>
        <stop offset="1" stop-color="#6f9c3c"/>
      </linearGradient>
    </defs>
    <rect x="276" y="250" width="196" height="361" fill="var(--green-pale)"/>
    <rect x="0" y="0" width="220" height="110" fill="var(--green)"/>
    <circle cx="90" cy="100" r="145" fill="var(--green)"/>
    <circle cx="317" cy="62" r="215" fill="var(--green)"/>
    <circle role="img" aria-label="Photo of a stone entrance sign framed by flowering garden beds" cx="317" cy="62" r="188" fill="url(#gardenGrad)"/>
  </svg>

  <div class="stats">
    <p class="stats__item">Our EMR<br>Safety rating<br>of .72</p>
    <p class="stats__item">Our average<br>commercial<br>landscape installation<br>size is $215,000</p>
    <p class="stats__item">Our largest completed<br>commercial landscape<br>installation in 2020<br>$1,375,590</p>
  </div>

  <div class="services">
    <h2 class="section-title">Our Commerical<br>Landscaping services</h2>
    <ul class="bullets">
      <li>Landscape Design &amp; Installation</li>
      <li>Seasonal Color</li>
      <li>Raingardens</li>
      <li>Bio Retention Ponds</li>
      <li>Tree Pruning, Trimming &amp; Removal</li>
      <li>Mulch Applicaton</li>
      <li>Native Prairie Restorations</li>
      <li>Landscape Lighting</li>
    </ul>
  </div>

  <p class="services__copy">Greenway Grounds will design and install the landscape of your choice, whether your taste includes the formal, manicured look of and estate garden, the whimsical color of an English cottage garden, the peaceful tranquility of an oriental Zen retreat or any other landscape specific to your tastes. Our qualified and professional designers will take into account your personal taste as well as the architecture of your home and the prevailing look and feel of the community.</p>

  <div class="clients">
    <h2 class="section-title">Our Clients</h2>
    <ul class="bullets">
      <li>Alder Brothers</li>
      <li>Northgate Precision Group</li>
      <li>Bright Path Service Corp</li>
      <li>CRW Construction</li>
      <li>Silver Ridge Construction</li>
      <li>Dalton Construction</li>
      <li>Eastfield Heavy Construction</li>
      <li>Fairway Concrete Construction</li>
      <li>Harbor Interchange Constructors</li>
      <li>Ironvale</li>
      <li>Jensen Enterprises</li>
      <li>Keel Construction</li>
      <li>Lumaro</li>
      <li>Nolan Pierce Brothers</li>
      <li>Oaktree Corporation</li>
      <li>Prairie Excavating</li>
      <li>QR Builders</li>
      <li>Rowan and Sons</li>
      <li>Stafford Electric</li>
      <li>Trailhead Construction</li>
      <li>Upland Construction</li>
    </ul>
  </div>

  <footer class="contact">
    <div class="contact__col contact__col--company">
      <p class="contact__label">CONTACT</p>
      <p>GREENWAY GROUNDS INC.</p>
      <p>4810 W 62nd Terrace</p>
      <p>Lakeview, KS 66210</p>
    </div>
    <span class="contact__rule"></span>
    <div class="contact__col contact__col--offices">
      <p class="contact__label">Lakeview Office</p>
      <p>1-555-320-4417</p>
      <p class="contact__label">Riverton Office</p>
      <p>1-555-218-6093</p>
    </div>
    <p class="contact__web">www.greenwaygrounds.com</p>
  </footer>
</section>

</body>
</html>
```